Redesign Company Website

Cellar Bridge new website: www.cellarbridge.example.com.au

Brief

• Cellar Bridge
Cellar Bridge is a relationship marketing company offering telesales services to partner wineries. We manage the winery’s database, engage in telesales campaigns and return great sales results to the winery.
Cellar Bridge currently operates in Australia, New Zealand and Canada, with plans to expand to the USA in 2014.

• The service
We take the winery’s database, clean it up, and typically run 2 telesales campaigns per year. The timing, products and pricing are agreed with the winery prior to the campaign.
There are multiple benefits for the winery: the database is engaged with the winery, sales conversions are high and the database is reliable and up to date.

• The size of the company
Cellar Bridge International employs about 20 people and plans to grow to 30. The turnover is in excess of AU$5m

• How long have you been established?
Cellar Bridge was rebranded 12 months ago, but the original entity has been trading for 10 years.

• The company in a few words
Dynamic
Responsive
Detailed
Bright
Independent
Friendly
Engaging

The old web site

www.cellarbridge.example.com.au

• What is good about the web site?
Clean look, succinct. No need to scroll down to get information.

• What don’t you like about the old web site?
Blocky top graphics look too cartoon-like
Stock photos
Dull, corporate look with no personality
Bad infographic on Services page
Limited contact information
Too much red

The new web site

• Outline the aims of the new web site
The main aim of the new website is to represent Cellar Bridge and its personality better. We hope to be able to engage wineries to come back to the site. It has to contain the relevant service and benefit information to convert new winery business.

• Who is the target audience?
This is above all a B2B website aimed at winery partners
It is not an e-commerce site, but we want wineries to come back frequently.

• How will your target audience be accessing your site
All forms, probably including mobile phones.

• What are the unique selling points for your company, your products or your services?
Independent
Reliable
Secure

• Competitors' web sites:
www.harvestcrewsample.com.au
http://www.morrowvaleestatesdirect.com.au/

The look and feel of the new web site

• Various web sites that we like the look & feel of.
http://www.tessbrook.com.au/ Great graphic on home page, good use of white space, uncluttered
http://pelvaquin.com/ Good use of space, clear navigation, bit quirky
http://www.casaremoli.com.au/ Ease of navigation, like the drop down “where we are” on the home page
http://www.starlanternrecaps.co.uk/ Great use of graphics for navigation etc.

• Logo and sample of corporate identity files attached.

Target Market(s)

Wineries in Australia, NZ, Canada, USA

Industry/Entity Type

E-Commerce

Requirements
Nice to have
• Would be good to have a blog on the site to create new content easily and frequently

```html
<!DOCTYPE html>
<html lang="en">
<head>
<meta charset="utf-8">
<title>Cellar Bridge</title>
<link href="https://fonts.googleapis.com/css2?family=Arimo:wght@400;700&family=Pinyon+Script&display=swap" rel="stylesheet">
<style>
  :root {
    --wood-dark: #2a1509;
    --wood-mid: #4a2814;
    --wood-light: #6b3a1c;
    --panel: rgba(28, 13, 5, 0.72);
    --nav: #1b0c04;
    --rule: #8a5a2c;
    --gold: #f2c230;
    --orange: #f08a1c;
    --brand-red: #d8241c;
    --cream: #f4e6cf;
    --text: #e9dcc6;
    --muted: #c9b79b;
    --social: #b8241a;
  }
  * { box-sizing: border-box; margin: 0; padding: 0; }
  html, body { width: 872px; height: 1200px; overflow: hidden; }
  body {
    position: relative;
    font-family: "Arimo", Arial, sans-serif;
    color: var(--text);
    background: linear-gradient(90deg, var(--wood-mid) 0%, var(--wood-light) 35%, var(--wood-mid) 65%, var(--wood-light) 100%);
  }
  .abs { position: absolute; }

  /* Header */
  .brand {
    left: 276px; top: 0; width: 334px; height: 140px;
    display: flex; align-items: center; justify-content: center;
  }
  .brand-name { font-weight: 700; font-size: 44px; color: var(--brand-red); letter-spacing: -0.5px; }
  .contact { right: 14px; top: 14px; text-align: right; }
  .contact .region { font-size: 11px; letter-spacing: 2px; color: var(--cream); }
  .contact .phone { font-size: 30px; font-weight: 700; color: #fff; margin-top: 6px; letter-spacing: 1px; }
  .contact .email { font-size: 11px; color: var(--cream); margin-top: 4px; }

  /* Navigation */
  .nav-bar {
    left: 0; width: 872px; height: 36px;
    background: var(--nav);
    border-top: 1px solid var(--rule); border-bottom: 1px solid var(--rule);
  }
  .nav-bar.top { top: 204px; }
  .nav-bar.bottom { top: 1150px; }
  .nav-bar ul { list-style: none; position: relative; height: 100%; }
  .nav-bar li {
    position: absolute; top: 0; line-height: 34px;
    font-size: 12px; font-weight: 700; color: #fff; letter-spacing: 0.5px;
  }
  .nav-bar li.sep { color: var(--muted); font-weight: 400; }

  /* Hero */
  .hero-visual {
    left: 520px; top: 250px; width: 230px; height: 230px; border-radius: 50%;
    background: radial-gradient(circle at 45% 40%, #c99a5e 0%, #7a4a22 55%, #3a1c0a 100%);
    border: 6px solid #5a3418;
  }
  .hero-copy { left: 64px; top: 330px; width: 440px; font-size: 11px; line-height: 15px; }
  .hero-copy h2 { font-size: 14px; color: var(--gold); margin-bottom: 2px; }
  .hero-copy h3 { font-size: 12px; color: var(--orange); margin: 14px 0 3px; }
  .hero-copy h3.gold { color: var(--gold); }
  .hero-copy p { color: var(--text); }

  /* Content panel */
  .panel { left: 20px; top: 520px; width: 832px; height: 610px; background: var(--panel); }

  .features { left: 50px; top: 530px; width: 780px; }
  .feature { position: absolute; top: 0; width: 190px; text-align: center; }
  .feature .thumb {
    width: 174px; height: 174px; border-radius: 50%; margin: 0 auto;
    border: 4px solid #7a4a22;
  }
  .feature h4 { font-size: 12px; color: var(--orange); margin: 12px 0 8px; }
  .feature p { font-size: 10px; line-height: 14px; text-align: left; color: var(--text); }

  .divider { left: 40px; top: 868px; width: 792px; height: 1px; background: var(--rule); }

  /* Welcome */
  .portrait {
    left: 58px; top: 890px; width: 174px; height: 190px;
    background: linear-gradient(160deg, #d8c2a0 0%, #8c6a48 60%, #4a3220 100%);
    border: 3px solid #7a4a22;
  }
  .welcome { left: 256px; top: 888px; width: 270px; }
  .welcome h2 { font-family: "Pinyon Script", cursive; font-weight: 400; font-size: 40px; color: var(--cream); line-height: 44px; }
  .welcome .label { font-size: 10px; color: var(--orange); letter-spacing: 1px; margin-top: -2px; }
  .welcome p { font-size: 10px; line-height: 14px; margin-top: 10px; }

  /* Testimonials */
  .testimonials { left: 600px; top: 890px; width: 200px; }
  .testimonials .label { font-size: 11px; color: var(--orange); letter-spacing: 1px; margin-left: 25px; }
  .quote-mark { position: absolute; font-size: 40px; font-weight: 700; color: #fff; line-height: 1; }
  .quote-mark.open { left: 0; top: 20px; }
  .quote-mark.close { right: -30px; top: 20px; }
  .testimonials p { font-size: 10px; line-height: 14px; margin: 14px 0 0 25px; }

  .social { left: 722px; top: 1088px; display: flex; gap: 10px; }
  .social span { width: 30px; height: 30px; background: var(--social); border-radius: 3px; display: block; }
</style>
</head>
<body>

<header>
  <div class="abs brand"><span class="brand-name">Cellar Bridge</span></div>
  <div class="abs contact">
    <div class="region">AUSTRALIA • NEW ZEALAND</div>
    <div class="phone">1800 555 019</div>
    <div class="email">info@cellarbridge.example.com.au</div>
  </div>
</header>

<nav class="abs nav-bar top">
  <ul>
    <li style="left:64px">HOME</li><li class="sep" style="left:112px">|</li>
    <li style="left:130px">ABOUT US</li><li class="sep" style="left:208px">|</li>
    <li style="left:228px">SERVICES</li><li class="sep" style="left:296px">|</li>
    <li style="left:312px">BENEFITS</li><li class="sep" style="left:384px">|</li>
    <li style="left:402px">TESTIMONIALS</li>
    <li class="sep" style="left:716px">|</li><li style="left:734px">CONTACT US</li>
  </ul>
</nav>

<div class="abs hero-visual" role="img" aria-label="Wine barrel end with a glass of red wine, grapes and vine leaves"></div>

<section class="abs hero-copy">
  <h2>Your Wine.</h2>
  <p>We sell it like we made it.</p>
  <h3>You make great wine. Leave the rest to us.</h3>
  <p>Our staff are highly trained in every aspect of your products and learn the values of your brand and what it represents. When your customers are contacted by Cellar Bridge, they will feel as if they had just spoken with a member of your own team.</p>
  <h3 class="gold">Cellar Bridge International.</h3>
  <p>Cellar Bridge is the first agency offering international service. We have offices in Australia, New Zealand and Canada. Ask us how we can help you in these countries and more.</p>
</section>

<div class="abs panel"></div>

<section class="abs features">
  <div class="feature" style="left:6px">
    <div class="thumb" role="img" aria-label="Bottles of new release wines" style="background:radial-gradient(circle,#e0b040,#6a3a14)"></div>
    <h4>NEW PRODUCTS</h4>
    <p>Lorem ipsum dolor sit amet, consectetur adipiscing elit, sed do eiusmod tempor incididunt ut labore et dolore magna aliqua. Ut enim ad minim veniam, quis nostrud exercitation ullamco laboris nisi ut aliquip ex ea commodo consequat.</p>
  </div>
  <div class="feature" style="left:198px">
    <div class="thumb" role="img" aria-label="Glasses of premium white wine" style="background:radial-gradient(circle,#f0d8a0,#7a4a22)"></div>
    <h4>PREMIUM WINES</h4>
    <p>Lorem ipsum dolor sit amet, consectetur adipiscing elit, sed do eiusmod tempor incididunt ut labore et dolore magna aliqua. Ut enim ad minim veniam, quis nostrud exercitation ullamco laboris nisi ut aliquip ex ea commodo consequat.</p>
  </div>
  <div class="feature" style="left:390px">
    <div class="thumb" role="img" aria-label="Red wine bottle and glass with grapes" style="background:radial-gradient(circle,#d8782a,#5a1c10)"></div>
    <h4>SPECIALS</h4>
    <p>Lorem ipsum dolor sit amet, consectetur adipiscing elit, sed do eiusmod tempor incididunt ut labore et dolore magna aliqua. Ut enim ad minim veniam, quis nostrud exercitation ullamco laboris nisi ut aliquip ex ea commodo consequat.</p>
  </div>
  <div class="feature" style="left:582px">
    <div class="thumb" role="img" aria-label="Wine rack filled with bottles" style="background:radial-gradient(circle,#8a5a3a,#2a140a)"></div>
    <h4>BEST SELLERS</h4>
    <p>Lorem ipsum dolor sit amet, consectetur adipiscing elit, sed do eiusmod tempor incididunt ut labore et dolore magna aliqua. Ut enim ad minim veniam, quis nostrud exercitation ullamco laboris nisi ut aliquip ex ea commodo consequat.</p>
  </div>
</section>

<div class="abs divider"></div>

<div class="abs portrait" role="img" aria-label="Portrait of the company director holding a glass of wine"></div>

<section class="abs welcome">
  <h2>Welcome</h2>
  <div class="label">MESSAGE</div>
  <p>Lorem ipsum dolor sit amet, consectetur adipiscing elit, sed do eiusmod tempor incididunt ut labore et dolore magna aliqua. Ut enim ad minim veniam, quis nostrud exercitation ullamco laboris nisi ut aliquip ex ea commodo consequat. Duis aute irure dolor in reprehenderit in voluptate velit esse.</p>
</section>

<section class="abs testimonials">
  <div class="label">TESTIMONIALS</div>
  <span class="quote-mark open">&ldquo;</span>
  <span class="quote-mark close">&rdquo;</span>
  <p>Lorem ipsum dolor sit amet, consectetur adipiscing elit, sed do eiusmod tempor incididunt ut labore et dolore magna aliqua. Ut enim ad minim veniam, quis nostrud exercitation ullamco laboris nisi ut aliquip ex ea commodo consequat.</p>
</section>

<div class="abs social" aria-label="Social links"><span></span><span></span><span></span></div>

<nav class="abs nav-bar bottom">
  <ul>
    <li style="left:140px">HOME</li><li class="sep" style="left:188px">|</li>
    <li style="left:206px">ABOUT US</li><li class="sep" style="left:284px">|</li>
    <li style="left:302px">SERVICES</li><li class="sep" style="left:372px">|</li>
    <li style="left:390px">BENEFITS</li><li class="sep" style="left:462px">|</li>
    <li style="left:480px">TESTIMONIALS</li><li class="sep" style="left:580px">|</li>
    <li style="left:598px">CONTACT US</li>
  </ul>
</nav>

</body>
</html>
```